Business Card Design

Tumble Nook is a Laundromat Store
we provide wash and Fold service to Customers who are busy with their life and can not come to the store and do laundry
we have customers who drop their laundry at the store
but now i want to provide service to customers who are not able to come to the store to drop. i will go to their address and pickup the laundry and get it washed folded and delivered
Updates
Can you use the colour in you design which i uploaded and also fusha fluorescent green bright pink
Target Market(s)
all works of life who don't have time to do laundry
Industry/Entity Type
Store
Contact Information for Business Card
TumbleNook Laundromat
284 Colbrook Street
Lynn MA 01957
Look and feel
Each slider illustrates characteristics of the customer's brand and the style your logo design should communicate.

```html
<!DOCTYPE html>
<html lang="en">
<head>
<meta charset="utf-8">
<title>Tumble Nook Laundromat – Pick-up Card</title>
<link rel="stylesheet" href="https://fonts.googleapis.com/css2?family=Roboto+Slab:wght@400;700&family=Roboto:wght@300;400&display=swap">
<style>
  :root {
    --page: #ececec;
    --lime-top: #d2f79a;
    --lime-mid: #b7f43c;
    --lime-bottom: #a4ef0c;
    --violet: #8a1df4;
    --magenta: #f01ed2;
    --ink: #111111;
    --white: #ffffff;
    --footer-lime: #c8f545;
  }
  * { margin: 0; padding: 0; box-sizing: border-box; }
  html, body { width: 1200px; height: 1000px; overflow: hidden; background: var(--page); }
  .card {
    position: absolute; left: 347px; top: 57px;
    width: 506px; height: 885px; overflow: hidden;
    font-family: "Roboto Slab", serif;
    text-align: center;
  }
  .card__top {
    position: absolute; left: 0; top: 0; width: 100%; height: 608px;
    background: linear-gradient(to bottom, var(--lime-top) 0%, var(--lime-mid) 55%, var(--lime-bottom) 100%);
  }
  .card__artwork {
    position: absolute; left: 0; top: 0; width: 100%; height: 420px;
    background: linear-gradient(to bottom, rgba(255,255,255,0.18), rgba(255,255,255,0));
  }
  .brand {
    position: absolute; left: 17px; top: 13px; width: 256px; height: 256px;
    border-radius: 50%; background: var(--white);
    display: flex; align-items: center; justify-content: center;
  }
  .brand__name {
    font-family: "Roboto Slab", serif; font-weight: 700;
    font-size: 36px; line-height: 1.1; color: var(--violet);
  }
  .line { position: absolute; left: 0; width: 100%; white-space: nowrap; }
  .headline-1 { top: 278px; font-size: 50px; font-weight: 700; letter-spacing: 2px; color: var(--ink); }
  .headline-2 { top: 330px; font-size: 46px; font-weight: 400; letter-spacing: 1px; color: var(--ink); }
  .offer-1 { top: 395px; font-size: 51px; font-weight: 400; color: var(--magenta); }
  .offer-2 { top: 451px; font-size: 51px; font-weight: 400; letter-spacing: 5px; color: var(--magenta); }
  .offer-1 b, .offer-2 b { font-weight: 700; }
  .offer-2 b { letter-spacing: 1px; }
  .body-1 { top: 521px; font-size: 25px; color: var(--ink); }
  .body-2 { top: 559px; font-size: 25px; color: var(--ink); }
  .body-2 b { font-weight: 700; }
  .card__contact {
    position: absolute; left: 0; top: 608px; width: 100%; height: 277px;
    background: var(--violet); color: var(--white);
  }
  .cta { top: 22px; font-size: 27px; }
  .cta b { font-weight: 700; }
  .phone { top: 70px; font-size: 60px; font-weight: 700; letter-spacing: 3px; font-family: "Roboto", sans-serif; }
  .divider {
    position: absolute; left: 0; top: 153px; width: 100%; height: 0;
    border-top: 2px dotted rgba(255,255,255,0.6);
  }
  .shop-name { top: 178px; font-family: "Roboto", sans-serif; font-weight: 300; font-size: 28px; letter-spacing: 4px; color: var(--footer-lime); }
  .shop-address { top: 222px; font-family: "Roboto", sans-serif; font-weight: 300; font-size: 25px; color: var(--footer-lime); }
</style>
</head>
<body>
  <div class="card">
    <div class="card__top">
      <div class="card__artwork" role="img" aria-label="Line drawing of clothes hanging on a clothesline"></div>
      <div class="brand"><span class="brand__name">Tumble<br>Nook</span></div>
      <p class="line headline-1">NO TIME</p>
      <p class="line headline-2">FOR WASHING?</p>
      <p class="line offer-1">WE NOW <b>PICK UP</b></p>
      <p class="line offer-2">FROM <b>YOU!</b></p>
      <p class="line body-1">We will pick up, wash, fold and</p>
      <p class="line body-2">return your clean laundry to <b>you</b>.</p>
    </div>
    <div class="card__contact">
      <p class="line cta"><b>Call us now</b> to lighten your load!</p>
      <p class="line phone">781-555-0148</p>
      <div class="divider"></div>
      <p class="line shop-name">TUMBLENOOK LAUNDROMAT</p>
      <p class="line shop-address">284 Colbrook Street • Lynn • MA 01957</p>
    </div>
  </div>
</body>
</html>
```